Bramble Peak Information Technology Business Card
Services for Move Add Change, Technical Relocation, Server Room Support, Technical Support
Bramble Peak Information Technology Business Card - Information Technology
Creative Brief
Professional
Owen Darlisk
2917 41st Lane Northeast Seattle WA 98422
owen@bramblepkit-example.com
www.bramblepkit-example.com
The original logo on the back, #34 and #35
Move Add and Changes, Corporate Relocation, Server Room Support, Technical Support

```html
<!DOCTYPE html>
<html lang="en">
<head>
<meta charset="utf-8">
<title>Bramble Peak Information Technology – Business Card</title>
<link rel="stylesheet" href="https://fonts.googleapis.com/css2?family=Open+Sans:wght@400;600;800&display=swap">
<style>
  :root {
    --page-bg: #e9e7e4;
    --card-white: #ffffff;
    --card-shade: #f1f1f1;
    --ink-dark: #2e2e2e;
    --ink-body: #3a3a3a;
    --swoosh-grey: #4a4a4a;
    --accent-orange: #f39419;
  }
  html, body {
    margin: 0;
    width: 1200px;
    height: 901px;
    overflow: hidden;
    background: var(--page-bg);
    font-family: "Open Sans", Arial, sans-serif;
  }
  .card {
    position: absolute;
    left: 110px;
    top: 170px;
    width: 980px;
    height: 560px;
    border-radius: 34px;
    overflow: hidden;
    background: radial-gradient(ellipse at 35% 45%, var(--card-white) 55%, var(--card-shade) 100%);
    box-shadow: 0 10px 30px rgba(0,0,0,0.18);
  }
  .card-swoosh {
    position: absolute;
    inset: 0;
    width: 980px;
    height: 560px;
  }
  .brand-name {
    position: absolute;
    left: 70px;
    top: 212px;
    margin: 0;
    font-size: 44px;
    font-weight: 800;
    letter-spacing: 0.5px;
    color: var(--ink-dark);
    text-transform: uppercase;
  }
  .address {
    position: absolute;
    left: 72px;
    top: 300px;
    margin: 0;
    font-size: 21px;
    line-height: 30px;
    color: var(--ink-body);
    font-style: normal;
  }
  .contact-list {
    position: absolute;
    left: 72px;
    top: 392px;
    margin: 0;
    padding: 0;
    list-style: none;
    font-size: 19px;
    color: var(--ink-body);
  }
  .contact-list li {
    display: flex;
    align-items: center;
    height: 34px;
  }
  .contact-icon {
    width: 18px;
    height: 18px;
    margin-right: 14px;
    fill: var(--accent-orange);
  }
  .holder {
    position: absolute;
    left: 560px;
    top: 168px;
  }
  .holder-name {
    margin: 0;
    font-size: 22px;
    font-weight: 600;
    letter-spacing: 0.5px;
    color: var(--accent-orange);
    text-transform: uppercase;
  }
  .holder-role {
    margin: 2px 0 0;
    font-size: 19px;
    color: var(--ink-body);
  }
</style>
</head>
<body>
  <article class="card">
    <svg class="card-swoosh" viewBox="0 0 980 560" aria-hidden="true">
      <path d="M640 0 L980 0 L980 560 L880 560 C905 320 830 110 640 0 Z" fill="var(--swoosh-grey)"/>
      <path d="M700 0 C860 70 950 260 945 560 L980 560 L980 0 Z" fill="#5a5a5a"/>
      <path d="M655 0 L980 0 L980 95 C900 45 790 12 655 0 Z" fill="var(--accent-orange)"/>
    </svg>

    <h1 class="brand-name">Bramble Peak</h1>

    <address class="address">
      2917 41st Lane NE,<br>
      Seattle WA 98422
    </address>

    <ul class="contact-list">
      <li>
        <svg class="contact-icon" viewBox="0 0 24 24"><path d="M6.6 10.8a15 15 0 0 0 6.6 6.6l2.2-2.2a1 1 0 0 1 1-.25 11.4 11.4 0 0 0 3.6.57 1 1 0 0 1 1 1V20a1 1 0 0 1-1 1A17 17 0 0 1 3 4a1 1 0 0 1 1-1h3.5a1 1 0 0 1 1 1c0 1.25.2 2.45.57 3.57a1 1 0 0 1-.25 1z"/></svg>
        012 555 0198
      </li>
      <li>
        <svg class="contact-icon" viewBox="0 0 24 24"><path d="M2 5h20v14H2z M2 5l10 8 10-8" fill="var(--accent-orange)" stroke="#fff" stroke-width="1.5"/></svg>
        owen@bramblepkit-example.com
      </li>
      <li>
        <svg class="contact-icon" viewBox="0 0 24 24"><circle cx="12" cy="12" r="10"/></svg>
        www.bramblepkit-example.com
      </li>
    </ul>

    <div class="holder">
      <p class="holder-name">Owen Darlisk</p>
      <p class="holder-role">Managing Director</p>
    </div>
  </article>
</body>
</html>
```